Business Card Design needed for logo design project

Our company needs a Business Card Design. Please refer to our original project in the link above.
Dorian Whitlock
Broker

W: Grandvistaestates.com
P: 214-555-0187
F: 267-555-0142
E: dorianwhitlock@ferncrestmail.com
A: North Dallas Office

Name Spelling update , sorry Dorian Whitlock card is double sided

```html
<!DOCTYPE html>
<html lang="en">
<head>
<meta charset="utf-8">
<title>Grand Vista Realty – Business Card</title>
<link href="https://fonts.googleapis.com/css2?family=Open+Sans:wght@400;600&display=swap" rel="stylesheet">
<style>
  :root {
    --backdrop: #6a4630;
    --card: #1c1c1c;
    --card-edge: #262626;
    --gold: #b39a6c;
    --green: #2fae74;
    --white: #f4f4f4;
    --divider: #555555;
  }
  * { margin: 0; padding: 0; box-sizing: border-box; }
  html, body {
    width: 1200px; height: 914px; overflow: hidden;
    background: var(--backdrop);
    font-family: "Open Sans", sans-serif;
  }
  .sheet {
    width: 1200px; height: 914px;
    display: flex; flex-direction: column;
    align-items: center; justify-content: center; gap: 40px;
  }
  .card {
    width: 700px; height: 400px;
    background: radial-gradient(circle at 50% 40%, var(--card-edge), var(--card) 70%);
    box-shadow: 0 10px 30px rgba(0,0,0,.45);
    position: relative;
  }
  .brand {
    display: flex; flex-direction: column; align-items: center; gap: 18px;
  }
  .brand-mark {
    width: 70px; height: 70px; border-radius: 50%;
    background: var(--gold);
  }
  .brand-name {
    font-weight: 600; font-size: 26px; letter-spacing: 2px;
    color: var(--gold); text-transform: uppercase; white-space: nowrap;
  }
  /* Office side */
  .card--office {
    display: flex; flex-direction: column; align-items: center; justify-content: center; gap: 34px;
  }
  .office-label { color: var(--white); font-size: 30px; font-weight: 400; }
  /* Contact side */
  .card--contact { display: flex; align-items: center; }
  .card--contact .brand { width: 340px; }
  .card--contact .brand-name { font-size: 22px; }
  .divider {
    width: 1px; height: 300px; background: var(--divider);
  }
  .person { padding-left: 44px; }
  .person-name { color: var(--gold); font-size: 30px; font-weight: 600; line-height: 1.1; }
  .person-role { color: var(--green); font-size: 21px; font-weight: 400; margin-bottom: 58px; }
  .contact-list { list-style: none; }
  .contact-list li {
    display: flex; align-items: center; gap: 14px;
    color: var(--white); font-size: 17px; line-height: 28px;
  }
  .contact-list svg { width: 18px; height: 18px; flex: none; }
</style>
</head>
<body>
<main class="sheet">
  <section class="card card--office">
    <div class="brand">
      <span class="brand-mark"></span>
      <span class="brand-name">Grand Vista Realty</span>
    </div>
    <p class="office-label">North Dallas Office</p>
  </section>

  <section class="card card--contact">
    <div class="brand">
      <span class="brand-mark"></span>
      <span class="brand-name">Grand Vista Realty</span>
    </div>
    <div class="divider"></div>
    <div class="person">
      <h1 class="person-name">Dorian Whitlock</h1>
      <p class="person-role">Broker</p>
      <ul class="contact-list">
        <li>
          <svg viewBox="0 0 20 20" aria-hidden="true"><circle cx="10" cy="10" r="8" fill="none" stroke="#2fae74" stroke-width="2"/><ellipse cx="10" cy="10" rx="3.5" ry="8" fill="none" stroke="#2fae74" stroke-width="1.5"/><line x1="2" y1="10" x2="18" y2="10" stroke="#2fae74" stroke-width="1.5"/></svg>
          Grandvistaestates.com
        </li>
        <li>
          <svg viewBox="0 0 20 20" aria-hidden="true"><path d="M4 2l4 1 1 4-2 2a11 11 0 0 0 4 4l2-2 4 1 1 4-3 2C8 18 2 12 2 5z" fill="#2fae74"/></svg>
          214-555-0187
        </li>
        <li>
          <svg viewBox="0 0 20 20" aria-hidden="true"><rect x="5" y="2" width="10" height="5" fill="#2fae74"/><rect x="2" y="7" width="16" height="8" rx="1" fill="#2fae74"/><rect x="5" y="12" width="10" height="6" fill="#1c1c1c" stroke="#2fae74" stroke-width="1.5"/></svg>
          267-555-0142
        </li>
        <li>
          <svg viewBox="0 0 20 20" aria-hidden="true"><rect x="2" y="4" width="16" height="12" fill="#2fae74"/><path d="M2 4l8 7 8-7" fill="none" stroke="#1c1c1c" stroke-width="1.5"/></svg>
          dorianwhitlock@ferncrestmail.com
        </li>
      </ul>
    </div>
  </section>
</main>
</body>
</html>
```